New Architectural Firm Business Cards

New Business card to compliment previous pixel forum logo (attached). Please design a business card that is simple, modern, creative....please do not use "symbols", simply the logo and associated graphics/text. The front should contain name/address/phone/email/web address (with graphics).....back should be 100% graphic design using the logo somehow. Hoping for a two color (black and yellow) design. full bleed design, no borders

Target Market(s)

Commercial Architecture Clients

Industry/Entity Type

Architecture

Contact Information for Business Card

Please design a business card that is simple, modern, creative....please do not use "symbols", simply the logo and associated graphics/text. The front should contain name/address/phone/email/web address (with graphics).....back should be 100% graphic design using the logo somehow

Font styles to use
Sans Serif

Colors
FFF300
FFF600
FEFA6F
FFFEC7
FFFEE8

Requirements
Must have
• Clean, Modern Design
Should not have
• Stock images or "icons"

```html
<!DOCTYPE html>
<html lang="en">
<head>
<meta charset="utf-8">
<title>pixel forum architecture — business card</title>
<link href="https://fonts.googleapis.com/css2?family=Archivo+Narrow:wght@600;700&family=Libre+Franklin:wght@500;600&display=swap" rel="stylesheet">
<style>
  :root {
    --backdrop: #c8c8c8;
    --card-yellow: #e0b114;
    --card-black: #050505;
    --ink: #111111;
    --brand-yellow: #e0b114;
    --paper-white: #f2f2f2;
    --stripe-grey: #9a9a9a;
  }
  * { margin: 0; padding: 0; box-sizing: border-box; }
  html, body {
    width: 1200px;
    height: 1101px;
    overflow: hidden;
    background: var(--backdrop);
  }
  .canvas {
    position: relative;
    width: 1200px;
    height: 1101px;
  }
  .card {
    position: absolute;
    width: 303px;
    height: 535px;
    overflow: hidden;
  }
  .card-front {
    left: 246px;
    top: 265px;
    background: var(--card-yellow);
    color: var(--ink);
  }
  .card-back {
    left: 641px;
    top: 264px;
    background: var(--card-black);
  }

  .holder-name {
    position: absolute;
    right: 26px;
    top: 68px;
    font-family: "Archivo Narrow", sans-serif;
    font-weight: 700;
    font-size: 29px;
    line-height: 32px;
    text-align: right;
    text-transform: uppercase;
  }
  .holder-role {
    position: absolute;
    right: 26px;
    top: 144px;
    font-family: "Libre Franklin", sans-serif;
    font-weight: 600;
    font-size: 14px;
    letter-spacing: 2px;
  }
  .web-address {
    position: absolute;
    left: 22px;
    top: 377px;
    transform: rotate(-90deg);
    transform-origin: left top;
    font-family: "Libre Franklin", sans-serif;
    font-weight: 600;
    font-size: 11.5px;
    letter-spacing: 1.4px;
    white-space: nowrap;
  }
  .contact-block {
    position: absolute;
    right: 22px;
    font-family: "Libre Franklin", sans-serif;
    font-weight: 600;
    font-size: 12.5px;
    line-height: 19px;
    letter-spacing: 1.3px;
    text-align: right;
    text-transform: uppercase;
  }
  .contact-address { top: 391px; }
  .contact-reach { top: 445px; }

  .pattern-field {
    position: absolute;
    left: 0;
    top: 0;
    width: 303px;
    height: 360px;
    background:
      radial-gradient(ellipse 110px 80px at 55px 55px, rgba(242,242,242,0.85), rgba(242,242,242,0) 100%),
      radial-gradient(ellipse 110px 170px at 225px 160px, rgba(224,177,20,0.7), rgba(224,177,20,0) 100%),
      radial-gradient(ellipse 120px 130px at 85px 255px, rgba(154,154,154,0.6), rgba(154,154,154,0) 100%),
      radial-gradient(ellipse 40px 40px at 40px 150px, rgba(224,177,20,0.5), rgba(224,177,20,0) 100%),
      linear-gradient(180deg, #0a0a0a 0%, #050505 100%);
  }
  .brand-name {
    position: absolute;
    left: 0;
    right: 0;
    top: 652px;
    top: 388px;
    font-family: "Archivo Narrow", sans-serif;
    font-weight: 700;
    font-size: 40px;
    line-height: 40px;
    color: var(--brand-yellow);
    text-align: center;
    text-transform: lowercase;
  }
</style>
</head>
<body>
  <main class="canvas">
    <section class="card card-front" aria-label="Card front">
      <h1 class="holder-name">Marcus<br>Ellery</h1>
      <p class="holder-role">OWNER</p>
      <p class="web-address">WWW.PIXELFORUM.COM</p>
      <p class="contact-block contact-address">Address Street 1565<br>Place, Zip Code 123456</p>
      <p class="contact-block contact-reach">012 456 7890<br>info@pixelforum.com</p>
    </section>

    <section class="card card-back" aria-label="Card back">
      <div class="pattern-field" role="img" aria-label="Large overlapping brand letterforms: solid white at top left, vertical yellow stripes at right, horizontal white stripes at lower left"></div>
      <p class="brand-name">pixel forum<br>architecture</p>
    </section>
  </main>
</body>
</html>
```